Whiskey Bottle Label Design

I need a label made for a short run whiskey bottle that will be given out as gifts.

I want it to look in a vintage style similar to the ones I have attached. I have also attached a file of the information I kind of want on it.

- I would like it on a vintage color label, maybe with a frame/border around it
- Limited edition
- Carrowden is the main title
- Charity Barrel Selection
- His signature
- Tennessee Whiskey

I would like to use the following sayings as a small written font (not exactly script like I have pictured, but more like hand writing) just repeating over and over.

"rent is due, pay the man • 2011 Pinehollow Invitational champion • only thing getting in the way is you • 2012 Red Mesa Classic champion • work hard, play hard • 2014 Harvest Lending Open champion • only easy day was yesterday"

I would like the Tennessee tri-star over it but maybe more sketched over it instead of just defined hard stars.

* This label has to look very high end. Also, it needs to be square in design. For colors, use a navy and red/crimson vintage look

```html
<!DOCTYPE html>
<html lang="en">
<head>
<meta charset="utf-8">
<title>Carrowden Charity Barrel Selection – Tennessee Whiskey Label</title>
<link rel="stylesheet" href="https://fonts.googleapis.com/css2?family=Rye&family=Smokum&family=Homemade+Apple&display=swap">
<style>
  :root {
    --label-blue: #0a14f0;
    --label-red: #ee1111;
    --ink: #111111;
    --paper: #ffffff;
  }
  * { margin: 0; padding: 0; box-sizing: border-box; }
  html, body { width: 1199px; height: 1200px; overflow: hidden; background: var(--paper); }
  .label { position: relative; width: 1199px; height: 1200px; background: var(--paper); }
  .label-art { position: absolute; inset: 0; }

  .banner-text {
    font-family: "Rye", serif;
    fill: var(--paper);
    stroke: var(--label-blue);
    stroke-width: 1;
    letter-spacing: 3px;
  }
  .banner-shadow { font-family: "Rye", serif; fill: #0a0f80; letter-spacing: 3px; }

  .brand-name { font-family: "Smokum", serif; }
  .brand-shadow { fill: var(--label-blue); }
  .brand-face { fill: var(--paper); stroke: var(--label-blue); stroke-width: 3.5; }

  .subtitle { font-family: "Rye", serif; fill: var(--ink); letter-spacing: 1.5px; }

  .signature {
    position: absolute; left: 463px; top: 515px; width: 298px; height: 106px;
    background: radial-gradient(ellipse at center, rgba(238,17,17,0.22), rgba(238,17,17,0) 70%);
  }

  .sayings {
    position: absolute; left: 267px; top: 648px; width: 666px; height: 436px;
    overflow: hidden;
    font-family: "Homemade Apple", cursive;
    font-size: 12.5px; line-height: 27.2px; color: var(--ink);
  }

  .tri-star-stamp {
    position: absolute; left: 463px; top: 739px; width: 248px; height: 248px;
    border-radius: 50%;
    border: 9px solid rgba(238,17,17,0.85);
    background: radial-gradient(circle, rgba(238,17,17,0.35), rgba(238,17,17,0.12) 70%);
  }

  .motto {
    position: absolute; height: 72px;
    font-family: "Rye", serif; font-size: 33px; line-height: 36px;
    color: var(--paper);
    -webkit-text-stroke: 1px var(--label-red);
    text-shadow: 3px 3px 0 var(--label-red);
    text-align: center; white-space: nowrap;
  }
  .motto-left { width: 422px; left: -63px; top: 833px; transform: rotate(90deg); letter-spacing: 5px; }
  .motto-right { width: 368px; left: 867px; top: 831px; transform: rotate(-90deg); letter-spacing: 6px; }
</style>
</head>
<body>
<main class="label">
  <svg class="label-art" width="1199" height="1200" viewBox="0 0 1199 1200">
    <defs>
      <path id="brand-arc" d="M120,505 Q597,395 1075,505"/>
      <path id="brand-arc-shadow" d="M125,510 Q602,400 1080,510"/>
      <path id="subtitle-arc" d="M262,551 Q602,430 943,551"/>
    </defs>

    <!-- label frame -->
    <path class="frame-outer" fill="none" stroke="var(--ink)" stroke-width="4"
      d="M92,62 H1107 A73,73 0 0 0 1180,135 V1095 A73,73 0 0 0 1107,1168 H92 A73,73 0 0 0 19,1095 V135 A73,73 0 0 0 92,62 Z"/>
    <path class="frame-inner" fill="none" stroke="var(--ink)" stroke-width="1.5"
      d="M97,68 H1102 A73,73 0 0 0 1174,140 V1090 A73,73 0 0 0 1102,1162 H97 A73,73 0 0 0 25,1090 V140 A73,73 0 0 0 97,68 Z"/>

    <!-- top banner -->
    <rect x="236" y="26" width="727" height="75" rx="37.5" fill="var(--paper)" stroke="var(--ink)" stroke-width="2"/>
    <rect x="239" y="29" width="721" height="69" rx="34.5" fill="var(--label-blue)"/>
    <text class="banner-shadow" x="602" y="83" font-size="44" text-anchor="middle">LIMITED EDITION</text>
    <text class="banner-text" x="599" y="80" font-size="44" text-anchor="middle">LIMITED EDITION</text>

    <!-- brand name -->
    <text class="brand-name brand-shadow" font-size="440">
      <textPath href="#brand-arc-shadow" startOffset="50%" text-anchor="middle" textLength="945" lengthAdjust="spacingAndGlyphs">CARROWDEN</textPath>
    </text>
    <text class="brand-name brand-face" font-size="440">
      <textPath href="#brand-arc" startOffset="50%" text-anchor="middle" textLength="945" lengthAdjust="spacingAndGlyphs">CARROWDEN</textPath>
    </text>

    <!-- subtitle -->
    <text class="subtitle" font-size="33">
      <textPath href="#subtitle-arc" startOffset="50%" text-anchor="middle" textLength="680" lengthAdjust="spacing">CHARITY BARREL SELECTION</textPath>
    </text>

    <!-- bottom banner -->
    <rect x="230" y="1115" width="727" height="75" rx="37.5" fill="var(--paper)" stroke="var(--ink)" stroke-width="2"/>
    <rect x="233" y="1118" width="721" height="69" rx="34.5" fill="var(--label-blue)"/>
    <text class="banner-shadow" x="597" y="1172" font-size="44" text-anchor="middle">TENNESSEE WHISKEY</text>
    <text class="banner-text" x="594" y="1169" font-size="44" text-anchor="middle">TENNESSEE WHISKEY</text>
  </svg>

  <div class="signature" role="img" aria-label="Handwritten signature in red ink"></div>

  <p class="sayings">Rent is due pay the man • 2011 Pinehollow Invitational champion • only thing getting in the way is you • 2012 Red Mesa Classic champion • work hard play hard • 2014 Harvest Lending Open champion • only easy day was yesterday Rent is due pay the man • 2011 Pinehollow Invitational champion • only thing getting in the way is you • 2012 Red Mesa Classic champion • work hard play hard • 2014 Harvest Lending Open champion • only easy day was yesterday Rent is due pay the man • 2011 Pinehollow Invitational champion • only thing getting in the way is you • 2012 Red Mesa Classic champion • work hard play hard • 2014 Harvest Lending Open champion • only easy day was yesterday Rent is due pay the man • 2011 Pinehollow Invitational champion • only thing getting in the way is you • 2012 Red Mesa Classic champion • work hard play hard • 2014 Harvest Lending Open champion • only easy day was yesterday</p>

  <div class="tri-star-stamp" role="img" aria-label="Distressed red circular stamp with three stars"></div>

  <div class="motto motto-left">RENT IS DUE<br>PAY THE MAN</div>
  <div class="motto motto-right">WORK HARD<br>PLAY HARD</div>
</main>
</body>
</html>
```